KT Fenwick's Brochure - Brevanta Solutions

Hello,
We have an example of very simple brochure (attached below). We would like you to make it better. More sophisticated. More professional looking. All of the info in the document needs to go in the brochure.
Please let me know if you can execute. I will be happy to send over photos, logos etc, once I know.

```html
<!DOCTYPE html>
<html lang="en">
<head>
<meta charset="utf-8">
<title>KT Fenwick – Brevanta Solutions Brochure</title>
<link rel="stylesheet" href="https://fonts.googleapis.com/css2?family=Barlow+Condensed:wght@300;400;500;600;700&display=swap">
<style>
  :root {
    --canvas: #58585a;
    --paper: #c4c4c6;
    --navy: #133f74;
    --accent: #1d4a8a;
    --ink: #1a1a1c;
    --white: #ffffff;
  }
  * { margin: 0; padding: 0; box-sizing: border-box; }
  html, body { width: 1200px; height: 848px; overflow: hidden; background: var(--canvas); }
  body { position: relative; font-family: "Barlow Condensed", "Arial Narrow", sans-serif; color: var(--ink); }

  .page {
    position: absolute; top: 120px; width: 467px; height: 604px;
    background: var(--paper); overflow: hidden;
  }
  .page--quality { left: 92px; }
  .page--design { left: 647px; }

  .header-band {
    position: absolute; left: 0; top: 54px; width: 100%; height: 59px;
    background: linear-gradient(90deg, #123b70 0%, #0c2b55 14%, #1c4682 30%, #3a5a94 42%, #123c72 56%, #2a4f8c 70%, #13407a 84%, #0f3566 100%);
  }
  .header-fade {
    position: absolute; left: 0; top: 113px; width: 100%; height: 60px;
    background: linear-gradient(180deg, #767679 0%, #a7a7aa 45%, var(--paper) 100%);
  }
  .page-title {
    position: absolute; left: 63px; top: 74px;
    font-weight: 300; font-size: 35px; color: var(--white); letter-spacing: -0.3px;
    transform: scaleX(0.74); transform-origin: left top; white-space: nowrap;
  }
  .page--design .page-title { left: 62px; }

  .brand-box {
    position: absolute; left: 340px; top: 40px; width: 85px; height: 71px;
    background: var(--white); display: flex; align-items: center; justify-content: center;
  }
  .brand-name { font-weight: 600; font-size: 15px; color: var(--accent); letter-spacing: 0.6px; }

  .photo { position: absolute; }
  .photo--chamber {
    left: 137px; top: 151px; width: 330px; height: 386px;
    background: linear-gradient(160deg, #3e4654 0%, #5d6a7a 35%, #8a95a0 60%, #4b4d52 100%);
  }
  .feature-panel {
    position: absolute; left: 60px; top: 131px; width: 181px; height: 427px;
    background: var(--navy); opacity: 0.95;
  }
  .feature-heading {
    position: absolute; left: 77px; top: 212px;
    font-weight: 600; font-size: 38px; line-height: 35px; color: var(--white); letter-spacing: -0.5px;
    transform: scaleX(0.8); transform-origin: left top; white-space: nowrap;
  }
  .feature-list { position: absolute; left: 77px; top: 301px; list-style: none; }
  .feature-list li {
    position: relative; padding-left: 12px; margin-bottom: 10px;
    font-weight: 400; font-size: 14px; line-height: 15.5px; color: var(--white);
  }
  .feature-list li::before {
    content: ""; position: absolute; left: 0; top: 3px; width: 5px; height: 5px;
    border-radius: 50%; background: var(--white);
  }
  .caption { position: absolute; left: 248px; top: 542px; font-size: 7px; color: var(--ink); }
  .foot-bar {
    position: absolute; left: 0; top: 571px; width: 275px; height: 8px;
    background: linear-gradient(90deg, #0d2a52 0%, #3c5690 35%, #8f96bf 50%, #2c4a86 70%, #0d2f5e 100%);
  }

  .intro {
    position: absolute; left: 64px; top: 140px; width: 350px;
    font-size: 17.6px; line-height: 20.6px; font-weight: 400;
  }
  .intro strong { font-weight: 600; color: var(--accent); }
  .col { position: absolute; top: 212px; }
  .col--resources { left: 64px; }
  .col--tools { left: 244px; }
  .col--tools-more { left: 363px; top: 234px; }
  .col-heading { font-size: 18px; font-weight: 400; line-height: 22px; }
  .col ul { list-style: none; }
  .col li { font-size: 13.6px; line-height: 18.3px; font-weight: 400; white-space: nowrap; }
  .photo--workshop {
    left: 0; top: 314px; width: 467px; height: 247px;
    background: linear-gradient(180deg, #2c45a0 0%, #3a4f9e 35%, #8e8c8d 65%, #b4b1ae 100%);
  }
  .contact-bar {
    position: absolute; left: 0; top: 571px; width: 100%; height: 8px;
    background: linear-gradient(90deg, #0f3262 0%, #1b3f78 50%, #10346a 100%);
    display: flex; gap: 19px; padding-left: 114px; align-items: center;
    font-size: 6.5px; color: var(--white);
  }
</style>
</head>
<body>

<section class="page page--quality">
  <div class="header-band"></div>
  <div class="header-fade"></div>
  <h1 class="page-title">Quality Control</h1>
  <div class="brand-box"><span class="brand-name">KT FENWICK</span></div>

  <div class="photo photo--chamber" role="img" aria-label="Photograph of the air and water test chamber with a tall glazed curtain wall unit in the factory"></div>
  <div class="feature-panel"></div>
  <h2 class="feature-heading">100% FACTORY<br>ASSEMBLED</h2>
  <ul class="feature-list">
    <li>Temperature Controlled<br>Clean Environment</li>
    <li>Lean Standard Work Training<br>and Certification</li>
    <li>Sealant Manufacture<br>Certification</li>
    <li>Rigorous Quality Inspections</li>
    <li>5% of Completed Units Tested<br>for Air &amp; Wate</li>
  </ul>
  <p class="caption">Air and Water Test Chamber</p>
  <div class="foot-bar"></div>
</section>

<section class="page page--design">
  <div class="header-band"></div>
  <div class="header-fade"></div>
  <h1 class="page-title">Design Assist</h1>
  <div class="brand-box"><span class="brand-name">KT FENWICK</span></div>

  <p class="intro">Through our <strong>Charrete Process</strong>, we work together with the entire team to identify the <strong>Owner's needs</strong>, the <strong>Architect's design intent</strong>, and the <strong>Contractor's schedule and budget</strong>.</p>

  <div class="col col--resources">
    <h3 class="col-heading">Resources We Provide :</h3>
    <ul>
      <li>Curtain Wall Designer Architect</li>
      <li>Structural Engineer Estimator</li>
      <li>Project Manager</li>
    </ul>
  </div>
  <div class="col col--tools">
    <h3 class="col-heading">Tools We Use:</h3>
    <ul>
      <li>Strukta for BIM Models</li>
      <li>Mind Map</li>
      <li>Document Tracking</li>
      <li>Product Samples</li>
    </ul>
  </div>
  <div class="col col--tools-more">
    <ul>
      <li>Decision Matrix</li>
      <li>Elevation Map</li>
      <li>Budget Updates</li>
    </ul>
  </div>

  <div class="photo photo--workshop" role="img" aria-label="Photograph of the design team in a charrette session at laptops around tables, with a presenter at a whiteboard"></div>
  <div class="contact-bar">
    <span>Website www.ktfenwickinc.com</span>
    <span>Phone 303-555-0147</span>
    <span>Fax 303-555-0162</span>
  </div>
</section>

</body>
</html>
```